Laundry Store front design

I own a laundry business and require a design for the shop front.

I have uploaded 3 photos with window numbers on, 1 thru 5. It might be better to stich these together as I want the design to flow across 1-5 but only the top of 3.

I have uploaded some pdf documents with more details.

Font styles to use
Serif

Colors
0054AA
0677BA
7BADD7
CADEEF
E8F1F8

```html
<!DOCTYPE html>
<html lang="en">
<head>
<meta charset="utf-8">
<title>Crestline Laundry Services – Shop Front Windows</title>
<link href="https://fonts.googleapis.com/css2?family=Roboto:wght@300;400;500;700;900&display=swap" rel="stylesheet">
<style>
  :root{
    --blue-deep:#0054AA;
    --blue:#0677BA;
    --blue-mid:#7BADD7;
    --blue-pale:#CADEEF;
    --blue-mist:#E8F1F8;
    --frame:#e6e6e6;
    --ink:#1a1a1a;
    --white:#ffffff;
  }
  *{box-sizing:border-box;margin:0;padding:0}
  html,body{width:738px;height:1200px;overflow:hidden;background:var(--white)}
  body{position:relative;font-family:'Roboto',sans-serif;color:var(--blue)}

  .brand{position:absolute;left:227px;top:44px;width:284px;text-align:center;color:var(--blue);font-weight:500}
  .brand__name{display:block;font-size:58px;line-height:58px;letter-spacing:1px}
  .brand__tag{display:block;font-size:21px;letter-spacing:3px;margin-top:4px;font-weight:400}
  .brand__dot{position:absolute;right:-4px;top:-10px;width:12px;height:12px;border-radius:50%;background:var(--blue)}

  .window{position:absolute;width:320px;height:256px;background:var(--frame);padding:5px;
    display:grid;grid-template-columns:84px 104px 105px;grid-template-rows:58px 181px;gap:6px 9px}
  .window--one{left:39px;top:192px}
  .window--two{left:379px;top:192px}
  .window--three{left:209px;top:534px}
  .window--four{left:40px;top:872px}
  .window--five{left:379px;top:872px}

  .pane{position:relative;overflow:hidden}
  .pane--white{background:var(--white)}

  /* one continuous photo per window, shown through each pane */
  .photo{background-image:var(--photo);background-size:320px 256px;background-repeat:no-repeat}
  .c1{background-position-x:-5px}
  .c2{background-position-x:-98px}
  .c3{background-position-x:-211px}
  .r1{background-position-y:-5px}
  .r2{background-position-y:-69px}

  .window--one{--photo:
    radial-gradient(ellipse 70px 55px at 140px 190px,#ffffff 0,#f3f1ec 45%,rgba(222,218,210,0) 100%),
    radial-gradient(ellipse 60px 55px at 255px 175px,#ffffff 0,#f1efea 45%,rgba(222,218,210,0) 100%),
    linear-gradient(180deg,#6e4322 0,#a8743e 4%,#d9c09a 7%,#f4f2ee 11%,#e4e1db 24%,#f6f5f2 34%,#dedbd4 46%,#eeece8 60%,#e2dfd9 78%,#f3f2ef 100%)}
  .window--two{--photo:
    radial-gradient(ellipse 40px 45px at 152px 30px,#c9603e 0,#d98a6c 40%,rgba(227,227,227,0) 100%),
    radial-gradient(ellipse 110px 70px at 130px 120px,#2748a8 0,#5b3f9e 30%,rgba(90,70,160,0) 100%),
    radial-gradient(ellipse 120px 55px at 150px 175px,#e3cb3a 0,#35a7c4 35%,#e26b3a 60%,rgba(200,160,120,0) 100%),
    linear-gradient(180deg,#e3e3e3 0,#e0e0e0 40%,#cfa47c 75%,#c9a07a 100%)}
  .window--three{--photo:
    radial-gradient(ellipse 55px 120px at 275px 150px,#14141f 0,#2c2b36 45%,rgba(44,43,54,0) 100%),
    radial-gradient(ellipse 90px 70px at 130px 110px,#efe6d6 0,#d9ccb6 50%,rgba(210,195,170,0) 100%),
    linear-gradient(180deg,#9a9895 0,#cdbda5 22%,#d8cab4 45%,#c9b497 62%,#cf3947 78%,#b92a38 100%)}
  .window--four{--photo:
    radial-gradient(ellipse 120px 70px at 100px 120px,#f6fbf5 0,rgba(230,243,232,0) 100%),
    radial-gradient(ellipse 110px 60px at 250px 200px,#d8ecdc 0,rgba(226,241,229,0) 100%),
    linear-gradient(160deg,#f1f7ee 0,#ddeedf 35%,#eef6ee 55%,#d9ecdd 80%,#e8f3e9 100%)}
  .window--five{--photo:
    linear-gradient(180deg,rgba(70,70,80,.55) 0,rgba(120,125,140,.25) 30%,rgba(255,255,255,0) 45%,rgba(20,30,70,.15) 100%),
    linear-gradient(100deg,#33509b 0,#e4e9f1 9%,#8592ad 17%,#f2f4f8 25%,#3e5fae 34%,#dbe3ef 42%,#2d4891 50%,#eef1f6 58%,#7b93c9 66%,#f1f3f7 74%,#3b5cb0 84%,#c9d4e8 92%,#2b4590 100%)}

  .copy{position:absolute;line-height:1.15}
  .copy--bold{font-weight:700}
  .copy--black{font-weight:900}

  .bullets{position:absolute;list-style:none}
  .bullets li{position:relative;padding-left:7px}
  .bullets li::before{content:"";position:absolute;left:0;top:.42em;width:4px;height:4px;border:1.2px solid var(--blue);border-radius:50%;background:var(--white)}

  .rule{position:absolute;height:1.5px;background:var(--blue)}

  .label-band{position:absolute;top:128px;height:40px;background:rgba(255,255,255,.55);
    font-size:26px;font-weight:700;line-height:40px;color:var(--blue);padding-left:6px;white-space:nowrap}

  .window-number{position:absolute;font-size:22px;font-weight:300;color:var(--ink)}
</style>
</head>
<body>

  <div class="brand">
    <span class="brand__name">crestline</span>
    <span class="brand__tag">Laundry Services</span>
    <span class="brand__dot"></span>
  </div>

  <!-- Window 1 -->
  <section class="window window--one">
    <div class="pane photo c1 r1" role="img" aria-label="Hotel bed with white pillows"></div>
    <div class="pane photo c2 r1" role="img" aria-label="Hotel bed with white pillows"></div>
    <div class="pane photo c3 r1" role="img" aria-label="Wooden headboard and pillows"></div>
    <div class="pane photo c1 r2" role="img" aria-label="White linen on a bed"></div>
    <div class="pane photo c2 r2" role="img" aria-label="Rolled white towels"></div>
    <div class="pane photo c3 r2" role="img" aria-label="Rolled white towel"></div>
    <p class="copy copy--bold" style="left:125px;top:31px;font-size:17px">Ask for</p>
    <p class="copy copy--bold" style="left:108px;top:76px;font-size:28px">special</p>
    <p class="copy copy--bold" style="left:108px;top:110px;font-size:28px">pricing</p>
    <p class="copy" style="left:221px;top:122px;font-size:7.5px;width:86px">commercial/business users</p>
    <ul class="bullets" style="left:9px;top:166px;font-size:7.5px;line-height:9.7px">
      <li>property managers,</li><li>hotels,</li><li>apartments,</li><li>villas,</li><li>restaurants<br>and more...</li>
    </ul>
  </section>

  <!-- Window 2 -->
  <section class="window window--two">
    <div class="pane photo c1 r1"></div>
    <div class="pane photo c2 r1" role="img" aria-label="Smiling woman with red hair"></div>
    <div class="pane photo c3 r1"></div>
    <div class="pane photo c1 r2" role="img" aria-label="Box of colourful laundry"></div>
    <div class="pane photo c2 r2" role="img" aria-label="Woman holding a box of colourful clothes"></div>
    <div class="pane photo c3 r2" role="img" aria-label="Woman's arm holding the box"></div>
    <p class="copy copy--bold" style="left:16px;top:27px;font-size:11.5px">Book online</p>
    <p class="copy copy--bold" style="left:227px;top:18px;font-size:17px;line-height:21px">collection<br>&amp; delivery</p>
    <svg style="position:absolute;left:253px;top:86px" width="18" height="16" viewBox="0 0 18 16"><path d="M0 0H18L9 16Z" fill="var(--blue)"/></svg>
    <p class="copy copy--bold" style="left:230px;top:107px;font-size:13.5px">Contact us:</p>
    <p class="copy copy--bold" style="left:216px;top:125px;font-size:8.5px">crestlinelaundry.example</p>
    <p class="copy copy--black" style="left:239px;top:153px;font-size:34px">20%</p>
    <p class="copy" style="left:237px;top:193px;font-size:6px">discount off for first order</p>
    <div class="rule" style="left:214px;top:220px;width:101px"></div>
    <p class="copy copy--bold" style="left:214px;top:226px;font-size:7.2px">Free delivery within local area</p>
    <div class="rule" style="left:214px;top:240px;width:101px"></div>
  </section>
  <span class="window-number" style="left:193px;top:460px">1</span>
  <span class="window-number" style="left:531px;top:460px">2</span>

  <!-- Window 3 -->
  <section class="window window--three">
    <div class="pane pane--white">
      <p class="copy" style="left:0;width:84px;top:17px;text-align:center;font-size:16px;font-weight:500">crestline</p>
      <p class="copy" style="left:0;width:84px;top:36px;text-align:center;font-size:5.5px;letter-spacing:.6px">Laundry Services</p>
    </div>
    <div class="pane photo c2 r1" role="img" aria-label="Laundry being loaded into a washing machine"></div>
    <div class="pane photo c3 r1" role="img" aria-label="Person loading a washing machine"></div>
    <div class="pane pane--white"></div>
    <div class="pane photo c2 r2" role="img" aria-label="Washing machine drum with red and beige clothes"></div>
    <div class="pane photo c3 r2" role="img" aria-label="Open washing machine door"></div>
    <p class="copy copy--bold" style="left:20px;top:74px;font-size:8px">555-014-2290</p>
    <p class="copy copy--bold" style="left:27px;top:120px;font-size:14px">Open</p>
    <p class="copy copy--bold" style="left:35px;top:140px;font-size:8px">9-19</p>
    <ul class="bullets" style="left:15px;top:169px;font-size:6.5px;line-height:8.2px">
      <li>Service washes,</li><li>Ironing service,</li><li>duvets,</li><li>linen,</li><li>towels,</li><li>wedding dresses,</li><li>upholstery,</li><li>rugs,</li><li>collection &amp; delivery</li>
    </ul>
  </section>
  <span class="window-number" style="left:362px;top:802px">3</span>

  <!-- Window 4 -->
  <section class="window window--four">
    <div class="pane pane--white"></div>
    <div class="pane pane--white"></div>
    <div class="pane pane--white"></div>
    <div class="pane photo c1 r2">
      <div role="img" aria-label="Hand-lettered word New with green leaves" style="position:absolute;left:10px;top:40px;width:64px;height:72px;border-radius:8px;background:linear-gradient(180deg,#9fd0a6 0,#7cbf86 55%,#b9debe 100%);opacity:.75"></div>
    </div>
    <div class="pane photo c2 r2" role="img" aria-label="Soft pale green fabric">
      <div role="img" aria-label="Green leaf" style="position:absolute;left:60px;top:40px;width:26px;height:20px;border-radius:50%;background:#a9d5af"></div>
      <p class="copy copy--bold" style="left:2px;width:100px;top:63px;text-align:center;font-size:18px">PureRinse</p>
      <p class="copy" style="left:2px;width:100px;top:86px;text-align:center;font-size:7.5px;letter-spacing:2.2px">WET CLEANING</p>
      <div class="rule" style="left:10px;top:101px;width:86px;height:1px"></div>
      <p class="copy" style="left:37px;top:106px;width:30px;text-align:center;font-size:5.5px;background:var(--blue);color:var(--white);border-radius:4px">Velora</p>
    </div>
    <div class="pane photo c3 r2" role="img" aria-label="Soft pale green fabric"></div>
    <ul class="bullets copy--bold" style="left:215px;top:118px;font-size:5.6px;line-height:7.5px">
      <li style="margin-bottom:7.8px">Specially adapted machines</li>
      <li style="margin-bottom:7.8px">Eco-friendly, no harsh chemicals</li>
      <li style="margin-bottom:7.8px">VIP 2 hour service available</li>
      <li style="margin-bottom:7.8px">Superior stain removal</li>
      <li>Suitable for all ‘dry clean only’<br>garments</li>
    </ul>
  </section>

  <!-- Window 5 -->
  <section class="window window--five">
    <div class="pane pane--white"></div>
    <div class="pane pane--white"></div>
    <div class="pane pane--white"></div>
    <div class="pane photo c1 r2" role="img" aria-label="Pressed shirts on hangers"></div>
    <div class="pane photo c2 r2" role="img" aria-label="Pressed checked shirts on hangers"></div>
    <div class="pane photo c3 r2">
      <div role="img" aria-label="Hand-lettered Same day service with a tick" style="position:absolute;left:50px;top:135px;width:50px;height:38px;border-radius:6px;background:rgba(255,255,255,.28)"></div>
    </div>
    <div class="label-band" style="left:7px;width:78px">Wash,</div>
    <div class="label-band" style="left:112px;width:78px;padding-left:10px">Dry &amp;</div>
    <div class="label-band" style="left:226px;width:76px;padding-left:15px">Fold</div>
  </section>
  <span class="window-number" style="left:193px;top:1143px">4</span>
  <span class="window-number" style="left:531px;top:1143px">5</span>

</body>
</html>
```